Business Card For Kelmora Financial Consulting

Hi, I would like a business card designed. Bold, modern.
Please use the same design as the logo. I have also attached the website design to see the overall theme.
Wordmark Font
Color: Hex: #01AEF7

```html
<!DOCTYPE html>
<html lang="en">
<head>
<meta charset="utf-8">
<title>Kelmora Financial Consulting – Business Card</title>
<link href="https://fonts.googleapis.com/css2?family=Montserrat:wght@400;500;700;800&display=swap" rel="stylesheet">
<style>
  :root {
    --stage: #e7e9ec;
    --card-dark: #15202b;
    --brand-blue: #01aef7;
    --text-light: #f2f5f8;
    --text-muted: #c9d3dc;
    --rule-blue: #1f6f96;
    --visual-teal: #5fd0e0;
    --visual-magenta: #c04fb4;
    --visual-navy: #13283a;
  }
  * { box-sizing: border-box; margin: 0; padding: 0; }
  html, body { width: 1200px; height: 900px; overflow: hidden; }
  body {
    background: var(--stage);
    font-family: "Montserrat", Arial, sans-serif;
    position: relative;
  }
  .card {
    position: absolute;
    left: 270px;
    width: 660px;
    height: 377px;
    overflow: hidden;
    background: var(--card-dark);
  }
  .card-front { top: 52px; border-radius: 44px 0 44px 0; }
  .card-back  { top: 471px; border-radius: 0 44px 0 44px; }

  .front-visual {
    position: absolute; inset: 0;
    background:
      linear-gradient(100deg, rgba(19,40,58,0) 30%, rgba(192,79,180,0.55) 48%, rgba(19,40,58,0) 60%),
      linear-gradient(100deg, rgba(19,40,58,0) 55%, rgba(95,208,224,0.75) 75%, rgba(19,40,58,0.2) 100%),
      linear-gradient(180deg, var(--visual-navy), #0f1e2b);
  }
  .brand {
    position: absolute;
    display: flex;
    align-items: center;
    gap: 14px;
  }
  .brand-square {
    width: 46px; height: 46px;
    border: 4px solid var(--brand-blue);
    flex: none;
  }
  .brand-name {
    color: var(--text-light);
    font-weight: 700;
    font-size: 22px;
    line-height: 1.15;
    letter-spacing: 0.02em;
    text-transform: uppercase;
  }
  .card-front .brand { left: 40px; top: 160px; }

  .holder { position: absolute; left: 48px; top: 52px; }
  .holder-name {
    color: var(--brand-blue);
    font-weight: 800;
    font-size: 27px;
    text-transform: uppercase;
  }
  .holder-role { color: var(--text-light); font-size: 18px; font-weight: 500; margin-top: 2px; }

  .contacts { position: absolute; left: 48px; top: 150px; list-style: none; }
  .contacts li {
    display: flex; align-items: center; gap: 10px;
    color: var(--text-light); font-size: 17px; margin-bottom: 10px;
  }
  .contacts svg { width: 18px; height: 18px; flex: none; }

  .divider {
    position: absolute; left: 48px; top: 268px;
    width: 330px; height: 1px; background: var(--rule-blue);
  }
  .card-back .brand { left: 48px; top: 290px; }

  .address {
    position: absolute; right: 40px; top: 150px;
    text-align: right; color: var(--text-light);
    font-size: 17px; line-height: 1.5;
  }
</style>
</head>
<body>
  <section class="card card-front">
    <div class="front-visual" role="img" aria-label="Abstract photograph of glowing glass towers in teal, pink and purple rising against a dark city grid"></div>
    <div class="brand">
      <span class="brand-square"></span>
      <span class="brand-name">Kelmora<br>Financial Consulting</span>
    </div>
  </section>

  <section class="card card-back">
    <div class="holder">
      <p class="holder-name">Lena Marsh</p>
      <p class="holder-role">Manager</p>
    </div>
    <ul class="contacts">
      <li>
        <svg viewBox="0 0 24 24" fill="var(--brand-blue)"><path d="M6.6 10.8a15.1 15.1 0 0 0 6.6 6.6l2.2-2.2a1 1 0 0 1 1-.25 11.4 11.4 0 0 0 3.6.57 1 1 0 0 1 1 1V20a1 1 0 0 1-1 1A17 17 0 0 1 3 4a1 1 0 0 1 1-1h3.5a1 1 0 0 1 1 1c0 1.25.2 2.45.57 3.57a1 1 0 0 1-.25 1z"/></svg>
        (025) 481 20573
      </li>
      <li>
        <svg viewBox="0 0 24 24" fill="none" stroke="var(--brand-blue)" stroke-width="2"><rect x="3" y="5" width="18" height="14" rx="2"/><path d="M3 7l9 6 9-6"/></svg>
        info@kelmoraconsulting.com
      </li>
      <li>
        <svg viewBox="0 0 24 24" fill="none" stroke="var(--brand-blue)" stroke-width="2"><circle cx="12" cy="12" r="9"/><path d="M3 12h18M12 3c3 3 3 15 0 18M12 3c-3 3-3 15 0 18"/></svg>
        www.kelmoraconsulting.com
      </li>
    </ul>
    <div class="divider"></div>
    <div class="brand">
      <span class="brand-square"></span>
      <span class="brand-name">Kelmora<br>Financial Consulting</span>
    </div>
    <p class="address">2218 Harlow Street<br>Brenton, FL 32507</p>
  </section>
</body>
</html>
```